New Letterhead

Improve the attached letterhead to make it more alive and corporate class using the company colors in the two companies logos available on the two companies website.

Industry/Entity Type

Construction Company

Requirements
Must have
• colours of the two logod
Nice to have
• Be more alive and professional
Should not have
• Any other colours besides the ones in the logos

```html
<!DOCTYPE html>
<html lang="en">
<head>
<meta charset="utf-8">
<title>Brandwell Letterhead</title>
<link rel="stylesheet" href="https://fonts.googleapis.com/css2?family=Source+Sans+3:wght@400;600;700&family=Arimo:wght@700&display=swap">
<style>
  :root {
    --backdrop: #e6e6e6;
    --paper: #ffffff;
    --ink: #3a3a3a;
    --ink-dark: #2b2d2f;
    --brand-red: #8b2a1f;
    --brand-teal: #2e9aa4;
    --rule: #9cc9cd;
  }
  * { margin: 0; padding: 0; box-sizing: border-box; }
  html, body { width: 1200px; height: 1200px; overflow: hidden; background: var(--backdrop); }
  .letterhead {
    position: absolute; left: 203px; top: 40px;
    width: 794px; height: 1120px;
    background: var(--paper);
    font-family: "Source Sans 3", sans-serif;
    color: var(--ink);
  }
  .brand {
    position: absolute; top: 62px; left: 0; width: 100%;
    display: flex; justify-content: center; align-items: center; gap: 10px;
  }
  .brand-mark { width: 22px; height: 22px; background: var(--brand-red); }
  .brand-name {
    font-family: "Source Sans 3", sans-serif; font-weight: 700;
    font-size: 38px; line-height: 1; letter-spacing: 1px; color: var(--ink-dark);
  }
  .greeting {
    position: absolute; left: 67px; top: 259px;
    font-family: "Arimo", sans-serif; font-weight: 700; font-size: 17px;
    color: #4a4a4a;
  }
  .letter-body { position: absolute; left: 68px; top: 297px; width: 664px; }
  .letter-body p {
    font-size: 16px; line-height: 20.7px; text-align: justify;
    margin-bottom: 21px; color: var(--ink);
  }
  .signature {
    position: absolute; left: 68px; top: 662px; width: 150px; height: 70px;
    background: linear-gradient(90deg, #f1f1f1, #e4e4e4);
    border-radius: 4px;
  }
  .contact-box {
    position: absolute; left: 45px; top: 1053px; width: 704px; height: 45px;
    border: 1px dashed var(--rule);
    display: flex; flex-direction: column; justify-content: center; align-items: center;
    font-size: 11px; line-height: 18px; color: #444;
  }
  .contact-box b { color: var(--brand-red); font-weight: 700; margin-left: 6px; }
  .contact-box b:first-child { margin-left: 0; }
  .footer-bar { position: absolute; top: 1107px; height: 13px; }
  .footer-bar.teal { left: 0; width: 396px; background: var(--brand-teal); }
  .footer-bar.red { left: 400px; width: 394px; background: var(--brand-red); }
</style>
</head>
<body>
  <main class="letterhead">
    <header class="brand">
      <span class="brand-mark"></span>
      <span class="brand-name">BRANDWELL</span>
    </header>

    <p class="greeting">Dear Mr. Dalton,</p>

    <section class="letter-body">
      <p>Lorem Ipsum is simply dummy text of the printing and typesetting industry. Lorem Ipsum has been the industry's standard dummy text ever since the 1500s, when an unknown printer took a galley of type and scrambled it to make a type specimen book. It has survived not only five centuries, but also the leap into electronic typesetting, remaining essentially unchanged.</p>
      <p>The standard chunk of Lorem Ipsum used since the 1500s is reproduced below for those interested. Sections 1.10.32 and 1.10.33 from "de Finibus Bonorum et Malorum" by Marcus Tellan are also reproduced in their exact original form, accompanied by English versions from the 1914 translation by H. Corwell</p>
      <p>Lorem Ipsum is simply dummy text of the printing and typesetting industry. Lorem Ipsum has been the industry's standard dummy text ever since the 1500s, when an unknown printer took a galley of type and scrambled it to make a type specimen book. It has survived not only five centuries, but also the leap into electronic typesetting, remaining essentially unchanged. It was popularised in the</p>
    </section>

    <div class="signature" role="img" aria-label="Handwritten signature of the sender"></div>

    <footer class="contact-box">
      <div><b>A.</b> 7 Marlow Street Fernvale, Eastbridge PO Box 51207, Oakdene, 3012 Westland <b>P.</b> +00 (0)21 555 0100 <b>W.</b> www.brandwell.com</div>
      <div><b>A.</b> 22 Kestrel Road, Cnr Harbour Avenue Hillcrest North, Eastbridge 4180 Westland <b>P.</b> +00 (0)21 555 0188 <b>W.</b> www.stonereach.com</div>
    </footer>
    <div class="footer-bar teal"></div>
    <div class="footer-bar red"></div>
  </main>
</body>
</html>
```